Label for natural soft drink / juice

Please see the briefing attached as PDF

Required is a label design that adds a frame for a range of different labels linked to a variety of tastes for a natural, organic, sparkling beverage in a multi-use, environmentally friendly returnable clear glass bottle.
The 2 first tastes are rhubarb and apple
The label will be a paper label sticked at the front side of the bottle.
No glossy or shiny appearance as it does not fit the organic image
No color restrictions in general, but
Blue better than green
Matt better than glossy
Fit of colours on one label essential, so no “crying colour mixture” (great also: complementary contrasts like blue/orange)
Handpainted better than photorealistic
Simple better than overcrowded
Smart, funny intelligent a lot better than same standard as everywhere
For the image consider subtile reminiscence to the fruit or other stuff linked to the fruit (even “across 3 corners”, so a bit far away) as a nice additional asset

Target Market(s)

modern restaurants with high quality food, often with organic and regional products on the menu.

Font styles to use
Serif
Sans Serif
Script

Requirements
Nice to have
• the fruit of the current taste or something linked to the fruit as e.g. reminiscence to well known story or history of the fruit
Should not have
• too many elements on the label. simplicity is key

```html
<!DOCTYPE html>
<html lang="en">
<head>
<meta charset="utf-8">
<title>Haldens Golden Apple Label</title>
<link rel="stylesheet" href="https://fonts.googleapis.com/css2?family=Oswald:wght@700&family=Pinyon+Script&family=Old+Standard+TT&display=swap">
<style>
  :root {
    --band: #f1de88;
    --paper: #fefdf4;
    --gold: #e3c842;
    --gold-light: #f3dd72;
    --taupe: #9b9190;
  }
  * { margin: 0; padding: 0; box-sizing: border-box; }
  html, body {
    width: 1200px;
    height: 1200px;
    overflow: hidden;
    background: var(--paper);
  }
  .label {
    position: relative;
    width: 1200px;
    height: 1200px;
    background: var(--paper);
  }
  .band {
    position: absolute;
    left: 0;
    width: 100%;
    height: 65px;
    background: var(--band);
  }
  .band--top { top: 0; }
  .band--bottom { bottom: 0; }

  .crest {
    position: absolute;
    left: 460px;
    top: 146px;
    width: 282px;
    height: 140px;
  }

  .brand-name {
    position: absolute;
    left: 0;
    width: 100%;
    top: 288px;
    text-align: center;
    font-family: "Oswald", sans-serif;
    font-weight: 700;
    font-size: 156px;
    line-height: 1;
    letter-spacing: 14px;
    padding-left: 14px;
    color: var(--gold);
  }

  .tagline {
    position: absolute;
    left: 0;
    width: 100%;
    top: 484px;
    text-align: center;
    font-family: "Pinyon Script", cursive;
    font-size: 66px;
    line-height: 78px;
    color: var(--taupe);
    word-spacing: 14px;
  }

  .fruit {
    position: absolute;
    left: 447px;
    top: 649px;
    width: 320px;
    height: 312px;
  }

  .flavour {
    position: absolute;
    left: 0;
    width: 100%;
    top: 978px;
    text-align: center;
    font-family: "Old Standard TT", serif;
    font-size: 66px;
    line-height: 1;
    letter-spacing: 2px;
    color: var(--gold);
  }
</style>
</head>
<body>
  <main class="label">
    <div class="band band--top"></div>

    <svg class="crest" viewBox="0 0 282 140" role="img" aria-label="Ornament of hop cones, leaves and wheat ears">
      <defs>
        <radialGradient id="crestTone" cx="50%" cy="55%" r="55%">
          <stop offset="0%" stop-color="#9b9190" stop-opacity="0.55"/>
          <stop offset="100%" stop-color="#9b9190" stop-opacity="0"/>
        </radialGradient>
      </defs>
      <rect width="282" height="140" fill="url(#crestTone)"/>
    </svg>

    <h1 class="brand-name">HALDENS</h1>

    <p class="tagline">Natural Organic<br>Sparkling Beverage</p>

    <svg class="fruit" viewBox="0 0 320 312" role="img" aria-label="Hand-painted golden apple with stem and leaf">
      <defs>
        <radialGradient id="fruitTone" cx="50%" cy="55%" r="50%">
          <stop offset="0%" stop-color="#f3dd72"/>
          <stop offset="70%" stop-color="#e3c842"/>
          <stop offset="100%" stop-color="#e3c842" stop-opacity="0"/>
        </radialGradient>
      </defs>
      <rect width="320" height="312" fill="url(#fruitTone)"/>
    </svg>

    <h2 class="flavour">GOLDEN APPLE</h2>

    <div class="band band--bottom"></div>
  </main>
</body>
</html>
```